Retro Label for old fashioned soda

We need a label for soda we are having private labeled for our retro, 1950's ice cream shop www.thefrostyparlor.net I don't want the label to look like something from 2017 with a retro feel, but more like an original (possibly kinda cheesy) label you'd see from the 1950's with some of the old catch lines like "tastes great", "invigorating" or "it is refreshing!" The prominent brand should be the name of our ice cream shop, The Frosty Parlor. the soda is also pure cane sugar so it might be good to have that on somewhere

Label size is 2.4" wide by 4" tall. Here is an example of some retro labels from lookfindr. I attached on file to this contest but there are more here: https://www.lookfindr.net/results?q=retro+soda+label&id=8Hq2Lm4Pz7Vb1Kc9Xw3Rt6Yd0Ns5Jf2Ga8Ue4Ko1Mi7Bl3Wp9Dv6Qx2Hc5Zr0Ty8Fn4#img=Pk7Rw2Lx9Qm3:

The label will be the same for all the flavors with the exception of the flavor name changing somewhere on the label. These are the flavors

Root Beer
Orange
Black Cherry
Lemonade
Raspberry Lime -Rickey
White Birch Beer
Lemon Iced Tea
Vanilla Cream
Orange Cream
Sarsaparilla
Ginger Ale

• retro feel. authentic old fashioned look

```html
<!DOCTYPE html>
<html lang="en">
<head>
<meta charset="utf-8">
<title>The Frosty Parlor – Root Beer Soda Label</title>
<link rel="stylesheet" href="https://fonts.googleapis.com/css2?family=Marcellus+SC&family=Montserrat:wght@700&family=Passion+One:wght@700&display=swap">
<style>
  :root {
    --page-bg: #ffffff;
    --label-red: #e14a2f;
    --deep-red: #a5231b;
    --soda-red: #c9372a;
    --gold: #e8c266;
    --cream: #f7e6ad;
    --pale-gold: #f3dc97;
  }
  html, body {
    margin: 0;
    padding: 0;
    width: 1034px;
    height: 1200px;
    overflow: hidden;
    background: var(--page-bg);
  }
  .canvas {
    position: relative;
    width: 1034px;
    height: 1200px;
  }
  .soda-label {
    position: absolute;
    left: 191px;
    top: 46px;
    width: 652px;
    height: 1108px;
    display: block;
  }
  .label-ground { fill: var(--label-red); }
  .gold-frame { fill: none; stroke: var(--gold); stroke-width: 4; }
  .gold-rule { stroke: var(--gold); stroke-width: 3; }
  .dark-band { fill: var(--deep-red); stroke: var(--gold); stroke-width: 3; }
  .stripe { stroke: var(--gold); stroke-width: 2; }
  .diamond-outer { fill: var(--gold); }
  .diamond-inner { stroke: var(--deep-red); stroke-width: 3; }
  .slogan {
    font-family: "Marcellus SC", serif;
    font-size: 50px;
    fill: var(--cream);
  }
  .brand-name {
    font-family: "Montserrat", sans-serif;
    font-weight: 700;
    fill: var(--deep-red);
  }
  .cane-sugar {
    font-family: "Montserrat", sans-serif;
    font-weight: 700;
    font-size: 38px;
    letter-spacing: 2px;
    fill: var(--gold);
  }
  .soda-word {
    font-family: "Passion One", sans-serif;
    font-weight: 700;
    font-size: 240px;
    fill: var(--soda-red);
    stroke: var(--gold);
    stroke-width: 2.5;
  }
  .flavor-name {
    font-family: "Montserrat", sans-serif;
    font-weight: 700;
    font-size: 64px;
    letter-spacing: 2px;
    fill: var(--cream);
  }
</style>
</head>
<body>
<main class="canvas">
  <svg class="soda-label" viewBox="0 0 652 1108" xmlns="http://www.w3.org/2000/svg" aria-label="The Frosty Parlor root beer soda label">
    <defs>
      <linearGradient id="diamondFill" x1="0" y1="0" x2="0" y2="1">
        <stop offset="0" stop-color="#f9ebb6"/>
        <stop offset="1" stop-color="#eccb74"/>
      </linearGradient>
    </defs>

    <rect class="label-ground" x="0" y="0" width="652" height="1108"/>
    <rect class="gold-frame" x="10" y="10" width="632" height="1088"/>

    <!-- slogan band -->
    <rect class="dark-band" x="22" y="22" width="608" height="80"/>
    <text class="slogan" x="326" y="78" text-anchor="middle">TASTES GREAT!</text>

    <!-- upper stripes -->
    <g class="stripes">
      <line class="stripe" x1="22" y1="116" x2="630" y2="116"/>
      <line class="stripe" x1="22" y1="126" x2="630" y2="126"/>
      <line class="stripe" x1="22" y1="136" x2="630" y2="136"/>
      <line class="stripe" x1="22" y1="146" x2="630" y2="146"/>
      <line class="stripe" x1="22" y1="156" x2="630" y2="156"/>
      <line class="stripe" x1="22" y1="166" x2="630" y2="166"/>
      <line class="stripe" x1="22" y1="176" x2="630" y2="176"/>
    </g>

    <!-- lower stripes -->
    <g class="stripes">
      <line class="stripe" x1="22" y1="584" x2="630" y2="584"/>
      <line class="stripe" x1="22" y1="594" x2="630" y2="594"/>
      <line class="stripe" x1="22" y1="604" x2="630" y2="604"/>
      <line class="stripe" x1="22" y1="614" x2="630" y2="614"/>
      <line class="stripe" x1="22" y1="624" x2="630" y2="624"/>
      <line class="stripe" x1="22" y1="634" x2="630" y2="634"/>
      <line class="stripe" x1="22" y1="644" x2="630" y2="644"/>
    </g>

    <!-- brand diamond -->
    <polygon class="diamond-outer" points="326,118 642,390 326,662 10,390"/>
    <polygon class="diamond-inner" fill="url(#diamondFill)" points="326,142 614,390 326,638 38,390"/>
    <text class="brand-name" x="326" y="318" text-anchor="middle" font-size="40">THE</text>
    <text class="brand-name" x="326" y="412" text-anchor="middle" font-size="88">FROSTY</text>
    <text class="brand-name" x="326" y="478" text-anchor="middle" font-size="58">PARLOR</text>

    <!-- pure cane sugar -->
    <line class="gold-rule" x1="22" y1="674" x2="630" y2="674"/>
    <text class="cane-sugar" x="326" y="720" text-anchor="middle">PURE CANE SUGAR</text>
    <line class="gold-rule" x1="22" y1="742" x2="630" y2="742"/>

    <!-- soda -->
    <text class="soda-word" x="326" y="966" text-anchor="middle" textLength="540" lengthAdjust="spacingAndGlyphs">SODA</text>

    <!-- flavor band -->
    <line class="gold-rule" x1="22" y1="984" x2="630" y2="984"/>
    <rect class="dark-band" x="22" y="996" width="608" height="90"/>
    <text class="flavor-name" x="326" y="1064" text-anchor="middle">ROOT BEER</text>
  </svg>
</main>
</body>
</html>
```